RLK Northgate Card Design

I am a RLK public practitioner.
I need to include RLK logo.
Basically, I want a professional business card which will clearly promote my service

Industry/Entity Type

Business

Contact Information for Business Card

I do need my business name, telephone, mobile, email, fax, postal address & street address

```html
<!DOCTYPE html>
<html lang="en">
<head>
<meta charset="utf-8">
<title>RLK Northgate Business Card</title>
<link href="https://fonts.googleapis.com/css2?family=Questrial&family=Libre+Baskerville&display=swap" rel="stylesheet">
<style>
  :root {
    --backdrop: #d6d6d6;
    --card: #ffffff;
    --brand-blue: #1b5aa5;
    --brand-orange: #f08a1c;
    --badge-blue: #1e5aa8;
    --badge-yellow: #f7c62f;
    --ink: #3c3c3c;
    --tagline: #6a6a6a;
  }
  * { box-sizing: border-box; margin: 0; padding: 0; }
  html, body { width: 1200px; height: 900px; overflow: hidden; }
  body {
    background: var(--backdrop);
    font-family: "Questrial", sans-serif;
    color: var(--ink);
    position: relative;
  }
  .card {
    position: absolute;
    top: 300px;
    width: 520px;
    height: 300px;
    background: var(--card);
    border-radius: 22px;
    box-shadow: 0 6px 18px rgba(0,0,0,0.12);
  }
  .card--back { left: 50px; }
  .card--front { left: 630px; }

  .brand { position: absolute; }
  .brand__name {
    display: flex; align-items: center; gap: 10px;
    font-family: "Questrial", sans-serif;
    color: var(--brand-blue);
    line-height: 1;
  }
  .brand__mark { background: var(--brand-orange); display: block; }
  .brand__tagline {
    font-family: "Libre Baskerville", serif;
    color: var(--tagline);
    letter-spacing: 0.5px;
  }

  .card--back .brand { left: 26px; top: 58px; }
  .card--back .brand__name { font-size: 44px; }
  .card--back .brand__mark { width: 18px; height: 18px; }
  .card--back .brand__tagline { font-size: 12.5px; margin-top: 6px; padding-left: 28px; }

  .card--front .brand { left: 78px; top: 105px; }
  .card--front .brand__name { font-size: 66px; }
  .card--front .brand__mark { width: 26px; height: 26px; }
  .card--front .brand__tagline { font-size: 18px; margin-top: 8px; padding-left: 36px; }

  .badge {
    position: absolute; right: 30px; top: 62px;
    width: 188px; height: 80px; display: flex;
  }
  .badge__main { flex: 0 0 114px; background: var(--badge-blue); }
  .badge__side { flex: 1; background: var(--badge-yellow); }

  .divider {
    position: absolute; left: 0; right: 0; top: 162px;
    height: 10px; background: var(--brand-blue);
  }

  .contacts {
    position: absolute; top: 190px;
    list-style: none; font-size: 17px; line-height: 22px;
  }
  .contacts--phones { left: 22px; }
  .contacts--places { left: 232px; }
  .contacts li { display: flex; align-items: flex-start; gap: 3px; }
  .contacts .indent { padding-left: 24px; }
  .icon { width: 20px; height: 20px; flex: 0 0 20px; fill: var(--brand-blue); margin-top: 1px; }
</style>
</head>
<body>

<section class="card card--back" aria-label="Card back with contact details">
  <div class="brand">
    <div class="brand__name"><span class="brand__mark"></span>Northgate</div>
    <div class="brand__tagline">RLK PUBLIC PRACTITIONER</div>
  </div>
  <div class="badge" aria-label="Accreditation badge">
    <span class="badge__main"></span><span class="badge__side"></span>
  </div>
  <div class="divider"></div>

  <ul class="contacts contacts--phones">
    <li>
      <svg class="icon" viewBox="0 0 20 20" aria-hidden="true"><path d="M5 2l3 4-2 2c1 2.5 3.5 5 6 6l2-2 4 3-2 3C9 17 3 11 2 5z"/></svg>
      1720 418 306
    </li>
    <li>
      <svg class="icon" viewBox="0 0 20 20" aria-hidden="true"><rect x="5" y="1" width="10" height="18" rx="2"/><rect x="7" y="3.5" width="6" height="8" fill="#fff"/></svg>
      6931 507 284
    </li>
    <li>
      <svg class="icon" viewBox="0 0 20 20" aria-hidden="true"><rect x="5" y="1" width="10" height="6"/><rect x="1" y="7" width="18" height="9" rx="2"/><rect x="5" y="12" width="10" height="7" fill="#fff" stroke="#1b5aa5" stroke-width="1.5"/></svg>
      4472 360 915
    </li>
  </ul>

  <ul class="contacts contacts--places">
    <li>
      <svg class="icon" viewBox="0 0 20 20" aria-hidden="true"><rect x="1" y="4" width="18" height="12" rx="1.5"/><path d="M2 5l8 6 8-6" fill="none" stroke="#fff" stroke-width="1.6"/></svg>
      info@northgatecpa.com
    </li>
    <li>
      <svg class="icon" viewBox="0 0 20 20" aria-hidden="true"><path d="M10 1l9 8h-3v9h-4v-6H8v6H4V9H1z"/></svg>
      2715 Alder Row, London
    </li>
    <li>
      <svg class="icon" viewBox="0 0 20 20" aria-hidden="true"><path d="M10 1l9 8h-3v9h-4v-6H8v6H4V9H1z"/></svg>
      8342 Willow Bend Ct,
    </li>
    <li class="indent">Carmel, IN 46032</li>
  </ul>
</section>

<section class="card card--front" aria-label="Card front">
  <div class="brand">
    <div class="brand__name"><span class="brand__mark"></span>Northgate</div>
    <div class="brand__tagline">RLK PUBLIC PRACTITIONER</div>
  </div>
</section>

</body>
</html>
```